HOLTMARK Construction Services
Project: Stationary
Stationary
Simple
Derek Pannell
derek@hltservices-example.com
www.hltservices-example.com
Finalized Draft of the logo can be seen on the following URL: http://www.quillora-example.com/contests/business-logo-264. AI file will be uploaded soon. At the front of the business card the following text should be added design.engineer.build commercial.residential

```html
<!DOCTYPE html>
<html lang="en">
<head>
<meta charset="utf-8">
<title>HOLTMARK Construction Services – Business Cards</title>
<link href="https://fonts.googleapis.com/css2?family=Questrial&family=Arimo:wght@400;700&display=swap" rel="stylesheet">
<style>
  :root {
    --backdrop: #e9e7e4;
    --card-light: #ffffff;
    --card-dark-top: #6b6b6b;
    --card-dark-bottom: #3a3a3a;
    --footer-dark: #2e2e2e;
    --green: #8dc63f;
    --green-light: #a6d65a;
    --ink: #222222;
    --logo-grey: #5a5a5a;
    --logo-light: #eeeeee;
    --rule: #cfcfcf;
  }
  * { box-sizing: border-box; margin: 0; padding: 0; }
  html, body { width: 1200px; height: 751px; overflow: hidden; }
  body { background: var(--backdrop); position: relative; font-family: "Questrial", sans-serif; }

  .card {
    position: absolute;
    width: 564px;
    height: 320px;
    border-radius: 16px;
    overflow: hidden;
    box-shadow: 0 6px 18px rgba(0,0,0,0.25);
  }
  .card--light { left: 96px; top: 44px; background: var(--card-light); }
  .card--dark { left: 508px; top: 392px; background: linear-gradient(160deg, var(--card-dark-top), var(--card-dark-bottom)); }

  .brand { position: absolute; left: 26px; top: 28px; width: 250px; text-align: center; }
  .brand__dot { width: 86px; height: 86px; border-radius: 50%; margin: 0 auto 12px; background: var(--green); }
  .brand__name { font-size: 46px; letter-spacing: 1px; line-height: 1; }
  .brand__tag { font-size: 11px; letter-spacing: 2.4px; text-transform: uppercase; margin-top: 6px; }
  .card--light .brand__name, .card--light .brand__tag { color: var(--logo-grey); }
  .card--dark .brand__name, .card--dark .brand__tag { color: var(--logo-light); }
  .card--dark .brand__dot { background: var(--green-light); }

  .divider { position: absolute; left: 296px; top: 36px; width: 2px; height: 190px;
    background: linear-gradient(to bottom, transparent, var(--rule), transparent); }
  .card--dark .divider { background: linear-gradient(to bottom, transparent, #9a9a9a, transparent); }

  .person { position: absolute; left: 356px; top: 42px; }
  .person__name { font-family: "Arimo", sans-serif; font-weight: 700; font-size: 22px; color: var(--ink); white-space: nowrap; }
  .contact { position: absolute; left: 356px; top: 172px; font-family: "Arimo", sans-serif; font-size: 11.5px; line-height: 15px; color: var(--ink); white-space: nowrap; }
  .card--dark .person__name, .card--dark .contact { color: #ffffff; }
  .card--dark .contact { top: 184px; }

  .services { position: absolute; left: 0; right: 0; display: flex; background: var(--green); }
  .card--light .services { top: 250px; height: 44px; border-top: 3px solid #e2e2e2; }
  .card--dark .services { top: 254px; height: 36px; background: linear-gradient(to bottom, var(--green-light), var(--green)); }
  .services__item { flex: 1; display: flex; align-items: center; justify-content: center;
    font-size: 18px; color: var(--ink); text-transform: uppercase; letter-spacing: 0.5px; }
  .services__item + .services__item { border-left: 1px solid rgba(0,0,0,0.2); }

  .disciplines { position: absolute; left: 0; right: 0; top: 290px; height: 30px; display: flex; background: var(--footer-dark); }
  .disciplines__item { flex: 1; display: flex; align-items: center; justify-content: center;
    font-size: 13px; color: #cfcfcf; letter-spacing: 1px; text-transform: uppercase; }
  .disciplines__item + .disciplines__item { border-left: 1px solid #555; }
</style>
</head>
<body>
  <section class="card card--light" aria-label="Business card, light version">
    <div class="brand">
      <div class="brand__dot"></div>
      <div class="brand__name">HOLTMARK</div>
      <div class="brand__tag">Construction Services</div>
    </div>
    <div class="divider"></div>
    <div class="person"><p class="person__name">Derek Pannell</p></div>
    <div class="contact">
      <p>555.802.0147</p>
      <p>www.hltservices-example.com</p>
      <p>derek@hltservices-example.com</p>
    </div>
    <div class="services">
      <span class="services__item">Commercial</span>
      <span class="services__item">Homes</span>
      <span class="services__item">Renovation</span>
    </div>
  </section>

  <section class="card card--dark" aria-label="Business card, dark version">
    <div class="brand">
      <div class="brand__dot"></div>
      <div class="brand__name">HOLTMARK</div>
      <div class="brand__tag">Construction Services</div>
    </div>
    <div class="divider"></div>
    <div class="person"><p class="person__name">Derek Pannell</p></div>
    <div class="contact">
      <p>555.802.0147</p>
      <p>www.hltservices-example.com</p>
      <p>derek@hltservices-example.com</p>
    </div>
    <div class="services">
      <span class="services__item">Residential</span>
      <span class="services__item">Commercial</span>
    </div>
    <div class="disciplines">
      <span class="disciplines__item">Design</span>
      <span class="disciplines__item">Engineer</span>
      <span class="disciplines__item">Build</span>
    </div>
  </section>
</body>
</html>
```